new letterhead/envelope/business card design for law firm

please see attached pdf of current letterhead, envelope and business card. I am also attaching my new logo that I would like to be used. basically, I am looking to refresh and simplify my letterhead/stationary and business card, keeping the following in mind:

overall, I am going for the following look:

-simple,
-modern,
-classy,
-professional

Target Market(s)

law firm clients

Industry/Entity Type

Law Firm

Contact Information for Business Card

see attachment

Font styles to use
Sans Serif

Requirements
Must have
• overall, I am going for the following look:
• -simple,
• -modern,
• -classy,
• -professional
Nice to have
• same as above
Should not have
• no serif fonts

```html
<!DOCTYPE html>
<html lang="en">
<head>
<meta charset="utf-8">
<title>Harlow Law – Stationery</title>
<link rel="stylesheet" href="https://fonts.googleapis.com/css2?family=Exo+2:wght@400;500;600&display=swap">
<style>
  :root {
    --navy: #123f73;
    --green: #4a9b3f;
    --green-light: #93c98a;
    --ink: #1d2f4d;
    --grey: #6b6b6b;
    --paper: #ffffff;
    --backdrop: #e6e9ec;
  }
  * { box-sizing: border-box; margin: 0; padding: 0; }
  html, body { width: 1200px; height: 1200px; overflow: hidden; }
  body {
    background: var(--backdrop);
    font-family: "Exo 2", sans-serif;
    color: var(--ink);
    position: relative;
  }
  .sheet {
    position: absolute;
    background: var(--paper);
    box-shadow: 0 2px 10px rgba(0,0,0,.12);
    overflow: hidden;
  }
  .brand { display: flex; align-items: center; }
  .brand-dot { border-radius: 50%; background: var(--navy); flex: none; }
  .brand-name { font-weight: 600; color: var(--navy); letter-spacing: .02em; white-space: nowrap; }

  /* Letterhead */
  .letterhead { left: 60px; top: 40px; width: 420px; height: 544px; }
  .letterhead .corner-rule { position: absolute; left: 40px; top: 0; width: 6px; height: 30px; background: var(--navy); }
  .letterhead .brand { position: absolute; right: 36px; top: 36px; gap: 8px; }
  .letterhead .brand-dot { width: 28px; height: 28px; }
  .letterhead .brand-name { font-size: 18px; }
  .letterhead .footer-address { position: absolute; left: 36px; bottom: 62px; font-size: 8px; line-height: 11px; color: var(--grey); }
  .letterhead .footer-rule { position: absolute; left: 36px; right: 36px; bottom: 48px; height: 1px; background: #9a9a9a; }
  .letterhead .footer-dot { position: absolute; left: 50%; bottom: 40px; width: 18px; height: 18px; margin-left: -9px; border-radius: 50%; background: #3a3a3a; border: 2px solid #fff; box-shadow: 0 0 0 1px #9a9a9a; }
  .letterhead .footer-web { position: absolute; right: 36px; bottom: 24px; font-size: 8px; color: var(--grey); }

  /* Envelope */
  .envelope { left: 540px; top: 150px; width: 600px; height: 300px; }
  .envelope .brand { position: absolute; left: 48px; top: 48px; gap: 14px; }
  .envelope .brand-dot { width: 58px; height: 58px; }
  .envelope .brand-name { font-size: 34px; }
  .envelope .return-address { position: absolute; left: 120px; top: 108px; font-size: 11px; line-height: 15px; color: var(--navy); }

  /* Business cards */
  .card { top: 620px; width: 540px; height: 350px; }
  .card-front { left: 40px; }
  .card-back { left: 620px; }
  .card .brand { position: absolute; left: 30px; top: 28px; gap: 18px; }
  .card .brand-dot { width: 66px; height: 66px; }
  .card .brand-name { font-size: 34px; }
  .contact-list { position: absolute; left: 48px; top: 134px; list-style: none; font-size: 15px; font-weight: 500; color: var(--navy); }
  .contact-list li { display: flex; align-items: center; height: 21.5px; }
  .contact-list li.address { align-items: flex-start; height: auto; margin-top: 12px; line-height: 21.5px; }
  .contact-list svg { width: 14px; height: 14px; margin-right: 14px; flex: none; stroke: var(--navy); fill: none; stroke-width: 1.3; }
  .contact-list li.address svg { margin-top: 11px; }
  .signature { position: absolute; right: 48px; bottom: 20px; color: var(--navy); }
  .signature .name { font-size: 16px; font-weight: 500; letter-spacing: .03em; }
  .signature .licence { font-size: 13px; margin-top: 2px; }
  .edge-band { position: absolute; top: 0; bottom: 0; right: 0; width: 14px; background: var(--navy); }
  .edge-rule { position: absolute; top: 0; bottom: 0; right: 20px; width: 3px; background: var(--green); }
  .top-band { position: absolute; left: 0; right: 0; top: 0; height: 8px; background: var(--navy); }
  .top-rule { position: absolute; left: 0; right: 0; top: 11px; height: 2px; background: var(--green); }
  .hidden-defs { position: absolute; width: 0; height: 0; }
</style>
</head>
<body>

<svg class="hidden-defs" aria-hidden="true">
  <defs>
    <symbol id="icon-phone" viewBox="0 0 14 14"><circle cx="7" cy="7" r="6"/><path d="M4.5 4.2l1.3-.4.8 1.8-.8.6a4 4 0 0 0 2 2l.6-.8 1.8.8-.4 1.3c-3 .2-5.5-2.3-5.3-5.3z"/></symbol>
    <symbol id="icon-fax" viewBox="0 0 14 14"><rect x="1.5" y="6" width="11" height="6" rx="1"/><path d="M4 6V2h6v4M4 9h6"/></symbol>
    <symbol id="icon-web" viewBox="0 0 14 14"><circle cx="7" cy="7" r="6"/><path d="M1 7h12M7 1c2.4 2.5 2.4 9.5 0 12M7 1c-2.4 2.5-2.4 9.5 0 12"/></symbol>
    <symbol id="icon-mail" viewBox="0 0 14 14"><rect x="1" y="3" width="12" height="8.5"/><path d="M1 3l6 5 6-5"/></symbol>
    <symbol id="icon-pin" viewBox="0 0 14 14"><circle cx="7" cy="4" r="2.2"/><path d="M7 6.2V12M3 12.5h8"/></symbol>
  </defs>
</svg>

<section class="sheet letterhead" aria-label="Letterhead">
  <div class="corner-rule"></div>
  <div class="brand"><span class="brand-dot"></span><span class="brand-name">HARLOW LAW</span></div>
  <div class="footer-address">
    820 Cedar Ridge Road, Suite 210<br>
    Millbrook, NC 27000<br>
    Tel: 555.214.7360<br>
    Fax: 555.214.7361
  </div>
  <div class="footer-rule"></div>
  <div class="footer-dot"></div>
  <div class="footer-web">www.harlowlawpa.com</div>
</section>

<section class="sheet envelope" aria-label="Envelope">
  <div class="brand"><span class="brand-dot"></span><span class="brand-name">HARLOW LAW</span></div>
  <div class="return-address">
    820 Cedar Ridge Road, Suite 210<br>
    Millbrook, NC 27000
  </div>
</section>

<section class="sheet card card-front" aria-label="Business card, version one">
  <div class="edge-band"></div>
  <div class="edge-rule"></div>
  <div class="brand"><span class="brand-dot"></span><span class="brand-name">HARLOW LAW</span></div>
  <ul class="contact-list">
    <li><svg><use href="#icon-phone"/></svg>Tel:&nbsp; 555.214.7360</li>
    <li><svg><use href="#icon-fax"/></svg>Fax: 555.214.7361</li>
    <li><svg><use href="#icon-phone"/></svg>Cell: 555.308.4417</li>
    <li><svg><use href="#icon-web"/></svg>www.harlowlawpa.com</li>
    <li><svg><use href="#icon-mail"/></svg>dan@harlowlawpa.com</li>
    <li class="address"><svg><use href="#icon-pin"/></svg><span>820 Cedar Ridge Road, Suite 210<br>Millbrook, NC 27000</span></li>
  </ul>
  <div class="signature">
    <div class="name">DANIEL R. HARLOW, ESQ.</div>
    <div class="licence">Licensed in NC and FL</div>
  </div>
</section>

<section class="sheet card card-back" aria-label="Business card, version two">
  <div class="top-band"></div>
  <div class="top-rule"></div>
  <div class="brand"><span class="brand-dot"></span><span class="brand-name">HARLOW LAW</span></div>
  <ul class="contact-list">
    <li><svg><use href="#icon-phone"/></svg>Tel:&nbsp; 555.214.7360</li>
    <li><svg><use href="#icon-fax"/></svg>Fax: 555.214.7361</li>
    <li><svg><use href="#icon-phone"/></svg>Cell: 555.308.4417</li>
    <li><svg><use href="#icon-web"/></svg>www.harlowlawpa.com</li>
    <li><svg><use href="#icon-mail"/></svg>dan@harlowlawpa.com</li>
    <li class="address"><svg><use href="#icon-pin"/></svg><span>820 Cedar Ridge Road, Suite 210<br>Millbrook, NC 27000</span></li>
  </ul>
  <div class="signature">
    <div class="name">DANIEL R. HARLOW, ESQ.</div>
    <div class="licence">Licensed in NC and FL</div>
  </div>
</section>

</body>
</html>
```